Providing Back Office Solutions to Financial Advisors and Attorney Needs a Business Card Design

Need a Business Card Design that speaks to Financial Advisor and Attorneys. Some of the word that come to mind is Clean/Simple & Futuristic.

Industry/Entity Type

Business

```html
<!DOCTYPE html>
<html lang="en">
<head>
<meta charset="utf-8">
<title>Norvane Business Card</title>
<link rel="stylesheet" href="https://fonts.googleapis.com/css2?family=Open+Sans:wght@400;600;700&display=swap">
<style>
  :root {
    --page-bg: #e6e8eb;
    --card-bg: #ffffff;
    --brand-blue: #1f6fae;
    --band-top: #0f5f9c;
    --band-bottom: #1a8bd0;
    --ink: #111111;
  }
  html, body {
    margin: 0;
    width: 1200px;
    height: 800px;
    overflow: hidden;
    background: var(--page-bg);
    font-family: "Open Sans", Arial, sans-serif;
  }
  .card {
    position: absolute;
    left: 150px;
    top: 143px;
    width: 900px;
    height: 514px;
    background: var(--card-bg);
    box-shadow: 0 10px 30px rgba(0,0,0,0.18);
    overflow: hidden;
  }
  .card-band {
    position: absolute;
    inset: 0;
  }
  .brand {
    position: absolute;
    left: 110px;
    top: 118px;
    display: flex;
    align-items: center;
    gap: 14px;
  }
  .brand-mark {
    width: 34px;
    height: 34px;
    background: var(--brand-blue);
  }
  .brand-name {
    font-weight: 600;
    font-size: 46px;
    letter-spacing: 3px;
    color: var(--brand-blue);
    line-height: 1;
  }
  .person {
    position: absolute;
    left: 290px;
    top: 236px;
  }
  .person-name {
    margin: 0;
    font-size: 30px;
    font-weight: 700;
    color: var(--brand-blue);
    line-height: 1.1;
  }
  .person-role {
    margin: 2px 0 0;
    font-size: 18px;
    color: var(--ink);
  }
  .contacts {
    position: absolute;
    left: 290px;
    top: 318px;
    margin: 0;
    padding: 0;
    list-style: none;
  }
  .contact {
    display: flex;
    align-items: center;
    gap: 12px;
    height: 34px;
    font-size: 21px;
    font-weight: 700;
    color: var(--ink);
  }
  .contact-icon {
    width: 20px;
    height: 20px;
    flex: none;
  }
</style>
</head>
<body>
  <main class="card">
    <svg class="card-band" width="900" height="514" viewBox="0 0 900 514" aria-hidden="true">
      <defs>
        <linearGradient id="band-fill" x1="0" y1="0" x2="0" y2="1">
          <stop offset="0" stop-color="var(--band-top)"/>
          <stop offset="1" stop-color="var(--band-bottom)"/>
        </linearGradient>
      </defs>
      <polygon points="0,0 44,0 44,205 76,240 190,240 258,322 258,432 210,514 0,514" fill="url(#band-fill)"/>
      <polyline points="56,0 56,198 82,226 196,226 272,316 272,438 226,514" fill="none" stroke="var(--brand-blue)" stroke-width="4"/>
    </svg>

    <div class="brand">
      <span class="brand-mark"></span>
      <span class="brand-name">NORVANE</span>
    </div>

    <section class="person">
      <h1 class="person-name">Daniel Marsh</h1>
      <p class="person-role">Director</p>
    </section>

    <ul class="contacts">
      <li class="contact">
        <svg class="contact-icon" viewBox="0 0 20 20" aria-hidden="true"><rect x="5" y="1" width="10" height="18" rx="2" fill="var(--brand-blue)"/><rect x="7" y="4" width="6" height="9" fill="#fff"/></svg>
        +61 400 128 372
      </li>
      <li class="contact">
        <svg class="contact-icon" viewBox="0 0 20 20" aria-hidden="true"><path d="M3 7h14v8H3z" fill="var(--brand-blue)"/><rect x="6" y="2" width="8" height="5" fill="var(--brand-blue)"/><rect x="6" y="12" width="8" height="6" fill="#fff" stroke="var(--brand-blue)" stroke-width="1.5"/></svg>
        +61 7 300 512 84
      </li>
      <li class="contact">
        <svg class="contact-icon" viewBox="0 0 20 20" aria-hidden="true"><rect x="1" y="4" width="18" height="12" rx="1.5" fill="var(--brand-blue)"/><path d="M2 5l8 6 8-6" fill="none" stroke="#fff" stroke-width="1.5"/></svg>
        info@norvaneoffice.com
      </li>
      <li class="contact">
        <svg class="contact-icon" viewBox="0 0 20 20" aria-hidden="true"><circle cx="10" cy="10" r="8.5" fill="var(--brand-blue)"/><g fill="none" stroke="#fff" stroke-width="1.2"><ellipse cx="10" cy="10" rx="3.5" ry="8.5"/><path d="M1.5 10h17M3 6h14M3 14h14"/></g></svg>
        www.norvaneoffice.com
      </li>
    </ul>
  </main>
</body>
</html>
```